Personal Finance e-commerce website needs a simple budget design

Hello! I am starting to sell downloadable and printable budget planners, as shown in the attached file, for people to plan ahead on their personal finances. <br/><br/>I want to see a one-page design with similar columns (for example, "Expenses, Budget, and Actual"). I would also like to see the basic formula ("Net Income = Gross income - Total Expenses") somewhere on the design. Finally, I want the design to remain mostly minimalistic and simple for the average person to plan their personal monthly budgets.<br/><br/>However, other than that, the overall design, layout, and colors will be at the graphic designer's choice. If you have any questions for me, please let me know. Thank you for your time!

Industry/Entity Type

Financial Planning

Colors

Designer to choose colors to be used in the design.

Requirements
Must have
• I want to see a one-page design with similar columns (for example, "Expenses, Budget, and Actual").
• I want the design to remain mostly minimalistic and simple for the average person to plan their personal monthly budgets.
Nice to have
• I would also like to see the basic formula ("Net Income = Gross income - Total Expenses") somewhere on the design.

```html
<!DOCTYPE html>
<html lang="en">
<head>
<meta charset="utf-8">
<title>Basic Monthly Budget</title>
<link href="https://fonts.googleapis.com/css2?family=Playfair+Display:wght@800&family=Poppins:wght@400;600;700&display=swap" rel="stylesheet">
<style>
  :root {
    --backdrop: #15206e;
    --paper: #ececee;
    --ink: #231f20;
    --navy: #1f3193;
    --indigo: #3444a0;
    --violet: #6464b0;
    --periwinkle: #a3acd8;
    --cell: #d3d3d6;
    --band: #1f2f95;
  }
  * { box-sizing: border-box; margin: 0; padding: 0; }
  html, body { width: 1180px; height: 1200px; overflow: hidden; }
  body { background: var(--backdrop); font-family: "Poppins", sans-serif; color: var(--ink); position: relative; }

  .sheet {
    position: absolute; left: 161px; top: 38px;
    width: 780px; height: 1022px;
    background: var(--paper);
    transform: scale(1.1); transform-origin: 0 0;
  }
  .meta { position: absolute; left: 54px; top: 58px; font-size: 16px; display: flex; align-items: baseline; }
  .meta .blank { display: inline-block; border-bottom: 1.5px solid var(--ink); margin: 0 4px 0 4px; }
  .brand { position: absolute; right: 44px; top: 60px; font-size: 16px; font-weight: 600; letter-spacing: 6px; }
  .title {
    position: absolute; left: 52px; top: 104px;
    font-family: "Playfair Display", serif; font-weight: 800; font-size: 63px; letter-spacing: -0.3px;
  }

  .budget-table { position: absolute; left: 54px; top: 213px; width: 675px; display: grid; grid-template-columns: repeat(3, 219px); column-gap: 9px; }
  .col-head {
    position: relative; height: 50px; color: #fff; font-weight: 700; font-size: 20px;
    display: flex; align-items: center; justify-content: center;
  }
  .col-head::after {
    content: ""; position: absolute; left: 50%; bottom: -8px; transform: translateX(-50%);
    border-left: 8px solid transparent; border-right: 8px solid transparent; border-top: 8px solid inherit;
  }
  .col-head.category { background: var(--navy); }
  .col-head.category::after { border-top-color: var(--navy); }
  .col-head.budget { background: var(--indigo); }
  .col-head.budget::after { border-top-color: var(--indigo); }
  .col-head.actual { background: var(--violet); }
  .col-head.actual::after { border-top-color: var(--violet); }
  .col-hint {
    height: 72px; background: var(--cell); font-size: 15px;
    display: flex; align-items: center; justify-content: center;
  }
  .col-cells { display: flex; flex-direction: column; gap: 3px; margin-top: 3px; }
  .col-cells span { display: block; height: 46px; background: var(--cell); }
  .col-cells span:last-child { height: 50px; }

  .totals { position: absolute; left: 54px; top: 834px; width: 675px; }
  .totals-band {
    height: 44px; background: var(--periwinkle);
    display: grid; grid-template-columns: repeat(3, 1fr); align-items: center; text-align: center;
    font-weight: 600; font-size: 21px;
  }
  .totals-band div { position: relative; }
  .totals-band div::after {
    content: ""; position: absolute; left: 50%; bottom: -17px; transform: translateX(-50%);
    border-left: 6px solid transparent; border-right: 6px solid transparent; border-top: 6px solid var(--periwinkle);
  }
  .totals-notes {
    display: grid; grid-template-columns: repeat(3, 1fr); text-align: center;
    font-size: 12.5px; line-height: 17px; text-transform: uppercase; margin-top: 7px;
  }
  .totals-notes p:last-child { margin-top: 3px; }

  .footer-band {
    position: absolute; left: 0; bottom: 0; width: 100%; height: 57px; background: var(--band);
    color: #fff; font-size: 21px; display: flex; align-items: center; justify-content: center;
  }
  .footer-band strong { font-weight: 700; margin: 0 6px; }
</style>
</head>
<body>
  <main class="sheet">
    <div class="meta">Month<span class="blank" style="width:106px"></span>Year<span class="blank" style="width:126px;margin-left:2px"></span></div>
    <div class="brand">LORENZO BRAVIK</div>
    <h1 class="title">Basic Monthly Budget</h1>

    <section class="budget-table">
      <div class="column">
        <div class="col-head category">Custom Category</div>
        <div class="col-hint">Expenses (Category)</div>
        <div class="col-cells"><span></span><span></span><span></span><span></span><span></span><span></span><span></span><span></span><span></span><span></span></div>
      </div>
      <div class="column">
        <div class="col-head budget">Budget (USD)</div>
        <div class="col-hint">What you plan to spend</div>
        <div class="col-cells"><span></span><span></span><span></span><span></span><span></span><span></span><span></span><span></span><span></span><span></span></div>
      </div>
      <div class="column">
        <div class="col-head actual">Actual (USD)</div>
        <div class="col-hint">What you actually spent</div>
        <div class="col-cells"><span></span><span></span><span></span><span></span><span></span><span></span><span></span><span></span><span></span><span></span></div>
      </div>
    </section>

    <section class="totals">
      <div class="totals-band">
        <div>Net Income</div>
        <div>Gross Income</div>
        <div>Total Expenses</div>
      </div>
      <div class="totals-notes">
        <p>How much money<br>you kept</p>
        <p>How much money<br>you earned</p>
        <p>Actual<br>expenses</p>
      </div>
    </section>

    <footer class="footer-band">Visit us at<strong>lorenzobravik.com</strong>for personal financial advice!</footer>
  </main>
</body>
</html>
```